Business card design for Bront Engineering Qavo

We need a new business card design along with all the necessary to place an order. The company is Bront Engineering Qavo and we recently updated our logo.

```html
<!DOCTYPE html>
<html lang="en">
<head>
<meta charset="utf-8">
<title>Bront Engineering Qavo — Business Card</title>
<link href="https://fonts.googleapis.com/css2?family=Montserrat:wght@300;400;500;600;700&display=swap" rel="stylesheet">
<style>
  :root {
    --backdrop: #555555;
    --card: #333333;
    --yellow: #e0bb0b;
    --stone: #857d78;
    --stone-light: #9a938e;
    --text-grey: #9c9590;
  }
  * { box-sizing: border-box; margin: 0; padding: 0; }
  html, body { width: 960px; height: 1200px; overflow: hidden; }
  body {
    background: var(--backdrop);
    font-family: "Montserrat", Arial, sans-serif;
    position: relative;
  }
  .card {
    position: absolute;
    left: 100px;
    width: 760px;
    height: 434px;
    background: var(--card);
    border-radius: 22px;
    overflow: hidden;
    box-shadow: 0 10px 28px rgba(0,0,0,0.28);
  }
  .card--front { top: 130px; }
  .card--back { top: 636px; }
  .card__accent { position: absolute; inset: 0; width: 100%; height: 100%; }

  .front-frame {
    position: absolute;
    left: 140px; top: 96px;
    width: 480px; height: 196px;
    border: 2px solid var(--stone);
    background: var(--card);
    display: flex; align-items: center; justify-content: center;
  }
  .company-name {
    font-weight: 600;
    color: var(--stone-light);
    letter-spacing: 0.04em;
    text-transform: uppercase;
    white-space: nowrap;
    display: flex; align-items: center; gap: 12px;
    line-height: 1;
  }
  .company-name__mark { width: 14px; height: 14px; background: var(--yellow); flex: none; }
  .front-frame .company-name { font-size: 26px; }

  .back-brand { position: absolute; left: 48px; top: 92px; }
  .back-brand .company-name { font-size: 24px; }

  .contact-block {
    position: absolute;
    right: 48px; top: 132px;
    width: 360px;
    text-align: right;
  }
  .person-name {
    font-size: 27px; font-weight: 300; color: var(--text-grey);
    letter-spacing: 0.02em; text-transform: uppercase;
  }
  .person-name__first { font-weight: 700; color: var(--yellow); }
  .person-title { font-size: 15px; font-weight: 400; color: var(--text-grey); margin-top: 2px; }
  .rule { height: 2px; background: var(--yellow); margin: 12px 0 16px 40px; }
  .contact-line {
    display: flex; justify-content: flex-end; align-items: center; gap: 10px;
    font-size: 15px; font-weight: 500; color: var(--yellow);
    margin-top: 7px;
  }
  .contact-line svg { width: 18px; height: 18px; flex: none; }
  .contact-line--gap { margin-top: 22px; }
</style>
</head>
<body>

<section class="card card--front" aria-label="Card front">
  <svg class="card__accent" viewBox="0 0 760 434" role="img" aria-label="Decorative geometric accents in yellow and grey">
    <defs>
      <linearGradient id="frontAccent" x1="0" y1="1" x2="1" y2="0">
        <stop offset="0" stop-color="#e0bb0b" stop-opacity="0.55"/>
        <stop offset="1" stop-color="#857d78" stop-opacity="0.75"/>
      </linearGradient>
    </defs>
    <polygon points="330,434 430,300 760,240 760,434" fill="url(#frontAccent)"/>
  </svg>
  <div class="front-frame">
    <div class="company-name"><span class="company-name__mark"></span>Bront Engineering Qavo</div>
  </div>
</section>

<section class="card card--back" aria-label="Card back">
  <svg class="card__accent" viewBox="0 0 760 434" role="img" aria-label="Decorative geometric accents in yellow and grey">
    <defs>
      <linearGradient id="backAccent" x1="0" y1="0" x2="1" y2="1">
        <stop offset="0" stop-color="#e0bb0b" stop-opacity="0.8"/>
        <stop offset="1" stop-color="#857d78" stop-opacity="0.8"/>
      </linearGradient>
    </defs>
    <polygon points="0,250 470,384 420,434 0,434" fill="url(#backAccent)"/>
  </svg>

  <div class="back-brand">
    <div class="company-name"><span class="company-name__mark"></span>Bront Engineering Qavo</div>
  </div>

  <div class="contact-block">
    <p class="person-name"><span class="person-name__first">Dana</span> Whitcombe</p>
    <p class="person-title">Specialist Engineering Qavo</p>
    <div class="rule"></div>
    <p class="contact-line">
      <svg viewBox="0 0 24 24" fill="none" stroke="var(--yellow)" stroke-width="1.6"><path d="M5 3h4l2 5-3 2a12 12 0 0 0 6 6l2-3 5 2v4a2 2 0 0 1-2 2A17 17 0 0 1 3 5a2 2 0 0 1 2-2z"/></svg>
      555 0142 7730
    </p>
    <p class="contact-line contact-line--gap">
      <svg viewBox="0 0 24 24" fill="none" stroke="var(--yellow)" stroke-width="1.6"><circle cx="12" cy="12" r="9"/><path d="M3 12h18M12 3c3 3 3 15 0 18M12 3c-3 3-3 15 0 18"/></svg>
      www.brontengineeringqavo.com
    </p>
    <p class="contact-line">
      <svg viewBox="0 0 24 24" fill="none" stroke="var(--yellow)" stroke-width="1.6"><rect x="3" y="5" width="18" height="14"/><path d="M3 5l9 8 9-8"/></svg>
      brontengineeringqavo@mail.com
    </p>
  </div>
</section>

</body>
</html>
```